Fun Dry Cleaners Business Flyer

We need a 5.5x8.5 business flyer designed for a new dry cleaners based in Texas called "Copperleaf Dry Cleaners". The flyer needs to be 2 sided (no fold) with the front side containing advertising information (slogan, hours of operation, address, etc...) along with the attached logo. The back will need to include the services and prices. The dry cleaners is a sports themed dry cleaners and we occasionally give away free game tickets (pro football, basketball, baseball, college sports tickets and memorabilia also). The design should be fun like the logo but also professional and appealing. We have no particular restrictions on the colors to be used.

The following should be included

Address - 418 N Bramble Ln
Waco, TX, 76704

Two Day Service
Dry Cleaning
Shirts - $1.50
Complete Suits - $9.99
Blouse - $3.00
Jeans/Pants - $4.00
Jackets - $5.00
Alterations
and More...

Hours of Operation: Monday - Friday 7 am - 6pm
Saturday 10am - 4pm
Sunday - Closed

Target Market(s)

Adults 21 and over
Business Professionals
People who go to Church etc...
Students

Industry/Entity Type

Dry Cleaner

Font styles to use
Serif
Sans Serif
Decorative

Colors

Designer to choose colors to be used in the design.

Requirements
Must have
• Logo should be incorporated within the flyer and naturally flow with the design
• The following should be included
• Address - 418 N Bramble Ln
• Waco, TX, 76704
• Two Day Service
• Dry Cleaning
• Shirts $1.25
• Complete Suits $9.99
• Jeans $3.99
• Slacks $3.99
• Sport Coats $3..99
• Blouses $2.99
• Pullovers $3.49
• Dresses $9.99
• Alterations
• and More...
• Hours of Operation: Monday - Friday 7 am - 6pm
• Saturday 10am - 4pm
• Sunday - Closed
• Phone Number - 254-618-5207
Nice to have
• Fun Design but professional, nice color scheme and flow, address should be visible and not hidden on the flyer

```html
<!DOCTYPE html>
<html lang="en">
<head>
<meta charset="utf-8">
<title>Copperleaf Dry Cleaners – Flyer</title>
<link href="https://fonts.googleapis.com/css2?family=Luckiest+Guy&family=Kalam:wght@400;700&family=Lato:wght@400;700&display=swap" rel="stylesheet">
<style>
  :root{
    --page:#e4e6e8;
    --blue-light:#4aa3e0;
    --blue:#3f86cf;
    --blue-deep:#2f6fc0;
    --green:#2e9a3e;
    --green-dark:#1f7a2c;
    --green-bright:#5cbb3a;
    --ink:#111;
    --white:#fff;
    --pill:#f3f3f3;
    --strip:#222;
  }
  *{box-sizing:border-box;margin:0;padding:0}
  html,body{width:1200px;height:1200px;overflow:hidden}
  body{background:var(--page);position:relative;font-family:'Lato',sans-serif}

  .flyer{position:absolute;top:205px;height:792px;overflow:hidden;box-shadow:0 6px 18px rgba(0,0,0,.25)}

  /* front */
  .flyer--front{left:70px;width:520px;
    background:
      repeating-conic-gradient(from 0deg at 50% 45%, rgba(255,255,255,.07) 0deg 8deg, rgba(0,0,0,0) 8deg 16deg),
      radial-gradient(circle at 50% 45%, var(--blue-light) 0%, var(--blue) 55%, var(--blue-deep) 100%);}
  .brand{position:absolute;top:66px;left:0;width:100%;display:flex;justify-content:center;align-items:center;gap:10px}
  .brand__dot{width:34px;height:34px;border-radius:50%;background:var(--green-bright)}
  .brand__name{font-family:'Lato',sans-serif;font-weight:700;font-size:22px;color:var(--white)}
  .headline{position:absolute;left:0;width:100%;text-align:center;font-family:'Luckiest Guy','Impact',sans-serif;line-height:1;white-space:nowrap}
  .headline--name{top:150px;font-size:58px;color:var(--white);-webkit-text-stroke:2px var(--ink);text-shadow:3px 3px 0 var(--ink)}
  .headline--trade{top:222px;font-size:52px;color:var(--blue-light);-webkit-text-stroke:2px var(--ink);text-shadow:3px 3px 0 var(--ink)}
  .stack-disc{position:absolute;left:94px;top:302px;width:272px;height:272px;border-radius:50%;
    background:radial-gradient(circle at 40% 40%, var(--green-bright), var(--green-dark));border:3px solid var(--ink)}
  .stack-photo{position:absolute;left:142px;top:334px;width:292px;height:210px;
    background:linear-gradient(180deg,#f08a3a 0%,#7f7f85 22%,#2f5f9a 38%,#d23a3a 58%,#55c8c8 78%,#67e0aa 100%);border-radius:6px}
  .hours{position:absolute;top:645px;left:23px;right:23px;display:flex;justify-content:space-between}
  .hours__pill{width:142px;height:60px;border-radius:16px;background:var(--pill);box-shadow:0 4px 6px rgba(0,0,0,.3);
    display:flex;flex-direction:column;justify-content:center;align-items:center;font-size:17px;line-height:1.25;color:var(--ink)}
  .address{position:absolute;top:730px;left:0;width:100%;display:flex;justify-content:center;align-items:center;gap:8px;color:var(--white);font-size:17px}

  /* back */
  .flyer--back{left:646px;width:522px;background:radial-gradient(circle at 50% 60%, var(--green-bright) 0%, var(--green) 55%, var(--green-dark) 100%)}
  .staff-photo{position:absolute;left:0;top:0;width:100%;height:370px;
    background:linear-gradient(110deg,#cbb497 0%,#d9c8b0 35%,#eef0f2 60%,#f4f4f4 100%)}
  .wave{position:absolute;left:0;top:0}
  .service{position:absolute;left:0;width:100%;text-align:center;font-family:'Luckiest Guy','Impact',sans-serif;line-height:1;white-space:nowrap}
  .service--days{top:350px;font-size:40px;color:var(--ink);text-shadow:2px 2px 0 var(--white),-1px -1px 0 var(--white)}
  .service--kind{top:400px;font-size:44px;color:var(--blue-light);-webkit-text-stroke:1.5px var(--ink);text-shadow:2px 2px 0 var(--ink)}
  .price{position:absolute;width:128px;height:128px;border-radius:50%;background:var(--white);border:5px solid var(--blue-deep);
    box-shadow:0 5px 10px rgba(0,0,0,.3);display:flex;flex-direction:column;align-items:center;justify-content:center;font-family:'Kalam',cursive}
  .price__icon{width:30px;height:30px;fill:var(--blue-deep)}
  .price__item{font-size:14px;color:var(--ink);line-height:1.1;margin-top:2px;white-space:nowrap}
  .price__cost{font-size:30px;font-weight:700;color:var(--green-dark);line-height:1.1}
  .website{position:absolute;top:752px;width:100%;text-align:center;font-family:'Kalam',cursive;font-weight:700;font-size:14px;color:var(--white)}
  .strip{position:absolute;bottom:0;left:0;width:100%;height:13px;background:var(--strip)}
</style>
</head>
<body>

<section class="flyer flyer--front">
  <div class="brand"><span class="brand__dot"></span><span class="brand__name">Copperleaf Dry Cleaners</span></div>
  <h1 class="headline headline--name">COPPERLEAF</h1>
  <h2 class="headline headline--trade">DRY CLEANERS</h2>
  <div class="stack-disc"></div>
  <div class="stack-photo" role="img" aria-label="Photo of a stack of neatly folded colourful clothes"></div>
  <div class="hours">
    <div class="hours__pill"><span>Monday - Friday</span><span>7 am - 6pm</span></div>
    <div class="hours__pill"><span>Saturday</span><span>10am - 4pm</span></div>
    <div class="hours__pill"><span>Sunday</span><span>Closed</span></div>
  </div>
  <div class="address">
    <svg width="26" height="26" viewBox="0 0 26 26" aria-hidden="true"><circle cx="13" cy="13" r="11.5" fill="none" stroke="#fff" stroke-width="2"/><path d="M7 13 L13 7.5 L19 13 M9 12 V18.5 H17 V12" fill="none" stroke="#fff" stroke-width="2" stroke-linejoin="round"/></svg>
    <span>418 N Bramble Ln Waco, TX, 76704</span>
  </div>
</section>

<section class="flyer flyer--back">
  <div class="staff-photo" role="img" aria-label="Photo of a smiling dry cleaner attendant beside a rack of suit jackets on hangers"></div>
  <svg class="wave" width="522" height="792" viewBox="0 0 522 792" aria-hidden="true">
    <path d="M0 318 Q200 268 522 340 L522 792 L0 792 Z" fill="#fff"/>
    <path d="M0 318 Q200 268 522 340" fill="none" stroke="#2f6fc0" stroke-width="6"/>
    <path d="M0 334 Q200 290 522 362 L522 792 L0 792 Z" fill="#2e9a3e"/>
  </svg>
  <div class="service service--days">TWO DAY SERVICE</div>
  <div class="service service--kind">DRY CLEANING</div>

  <div class="price" style="left:33px;top:463px">
    <svg class="price__icon" viewBox="0 0 30 30"><path d="M9 4 L4 8 L6 13 L9 11 V27 H21 V11 L24 13 L26 8 L21 4 Q15 8 9 4 Z"/></svg>
    <span class="price__item">SHIRTS</span><span class="price__cost">$1.50</span>
  </div>
  <div class="price" style="left:197px;top:463px">
    <svg class="price__icon" viewBox="0 0 30 30"><path d="M8 3 L13 3 L15 10 L17 3 L22 3 L26 8 V28 H17 L15 14 L13 28 H4 V8 Z"/></svg>
    <span class="price__item">COMPLETE SUITS</span><span class="price__cost">$9.99</span>
  </div>
  <div class="price" style="left:361px;top:463px">
    <svg class="price__icon" viewBox="0 0 30 30"><path d="M10 3 H12 Q15 9 18 3 H20 V9 Q24 14 23 28 H7 Q6 14 10 9 Z"/></svg>
    <span class="price__item">BLOUSE</span><span class="price__cost">$3.00</span>
  </div>
  <div class="price" style="left:101px;top:607px">
    <svg class="price__icon" viewBox="0 0 30 30"><path d="M8 3 H22 L23 28 H17 L15 11 L13 28 H7 Z"/></svg>
    <span class="price__item">JEANS/PANTS</span><span class="price__cost">$4.00</span>
  </div>
  <div class="price" style="left:293px;top:607px">
    <svg class="price__icon" viewBox="0 0 30 30"><path d="M10 3 H20 L26 8 V27 H19 V12 H17 V28 H13 V12 H11 V27 H4 V8 Z"/></svg>
    <span class="price__item">JACKETS</span><span class="price__cost">$5.00</span>
  </div>

  <div class="website">www.yourwebsite.com</div>
  <div class="strip"></div>
</section>

</body>
</html>
```